Ceramic worktop for laboratory furniture

We want a simple product catalog, maybe 4-8 pages, our ceramic worktop was chemical resistant, is a good worktop material for high chemicals corrosion environment like laboratory furniture, fumecupboard.

You can visit http://www.stonebenchwerk-demo.com/products/FERN%20BENCH%20SURFACE%20MATCHING%20PRODUCTS.html
https://www.facebook.com/500000000000001/videos/5000000000000002/?__so__=channel_tab&__rv__=all_videos_card

http://www.benchora-demo.com/products/lab-furniture-series/worktops#verticalTab3

https://www.quillmarkfitouts-demo.com/blog/laboratory-countertop-material/

https://resources.harlowbenchworks-demo.com/blog/top-5-materials-to-consider-for-your-lab-countertops

https://www.torvanex-demo.in/blog/type-of-laboratory-worktops-their-selection-criteria/

https://www.brenmoor-demo.com/Brenmoor/Literature/Blog/The-Different-Laboratory-Worksurfaces.htm

as reference

Target Market(s)

Asia, UAE and India

Industry/Entity Type

Laboratory fumecupboard and laboratory furniture manufacturer

Font styles to use
Sans Serif

Colors
00AB8E
00BBA5
67D7C9
C6EFE9
E9F9F6

Requirements
Must have
• This catalog mainly will sent to my customer handphone

```html
<!DOCTYPE html>
<html lang="en">
<head>
<meta charset="utf-8">
<title>Vantra Lab Supplies – Ceramic Worktop Catalog 2022</title>
<link rel="stylesheet" href="https://fonts.googleapis.com/css2?family=Anton&family=Montserrat:wght@400;500;600;700;800&display=swap">
<style>
:root{
  --board:#e4e3e8;
  --paper:#ffffff;
  --ink:#111111;
  --text:#333333;
  --green:#1aab3a;
  --orange:#f0921e;
  --orange-light:#f7b45a;
  --band:#ececf1;
  --row:#d9d8de;
  --dark:#3a3a3a;
}
*{box-sizing:border-box;margin:0;padding:0}
html,body{width:1200px;height:2400px;overflow:hidden;background:var(--board)}
body{font-family:"Montserrat",sans-serif;color:var(--text);position:relative}
.page{position:absolute;background:var(--paper);box-shadow:0 2px 6px rgba(0,0,0,.18);overflow:hidden}
.page *{position:absolute}
.page .flow, .page .flow *{position:static}
.cover{left:261px;top:114px;width:678px;height:877px}
.sheet{width:441px;height:570px}
.sheet-pp{left:116px;top:1095px}
.sheet-benchlyn{left:643px;top:1095px}
.sheet-categories{left:116px;top:1713px}
.sheet-back{left:643px;top:1713px}

/* brand lockup */
.brand{display:flex;align-items:center;gap:6px;font-family:"Montserrat",sans-serif;font-weight:800;color:var(--ink);white-space:nowrap}
.brand .brand-mark{position:static;background:var(--green)}
.brand span{position:static}

/* cover */
.cover-band{left:0;top:282px;width:678px;height:30px;background:var(--band)}
.cover-title{left:0;width:678px;text-align:center;font-family:"Anton",sans-serif;font-size:64px;line-height:1;top:194px;color:var(--ink);letter-spacing:-.5px}
.cover-sub{left:0;width:678px;text-align:center;top:262px;font-weight:700;font-size:45px;color:var(--green);letter-spacing:1px;line-height:1}
.cover-tag{left:94px;top:316px;width:489px;height:41px;background:var(--ink);color:#fff;font-weight:800;font-size:26px;letter-spacing:1.5px;display:flex;align-items:center;justify-content:center}
.photo{background:linear-gradient(160deg,#d9d9d9 0%,#bfbfc2 40%,#2b2b2b 55%,#e9e9ea 70%,#a9a9ab 100%)}
.cover-photo{left:0;top:390px;width:678px;height:361px}
.catalog-row{display:flex;align-items:center}
.catalog-word{font-weight:400;color:var(--ink);line-height:1}
.year{background:var(--green);color:#fff;font-weight:800;letter-spacing:3px;display:flex;align-items:center;justify-content:center}
.site{font-weight:700;color:var(--ink);white-space:nowrap}

/* inner sheets */
.frame{border:6px solid var(--orange);background:#fff}
.frame .shot{left:8px;top:8px;right:8px;bottom:8px;background:linear-gradient(180deg,#f3f3f3,#cfcfd3 50%,#7d7d85)}
.h-title{font-weight:800;color:var(--ink);line-height:1;white-space:nowrap}
.h-sub{font-weight:500;color:var(--orange);font-size:9.5px;letter-spacing:.4px;white-space:nowrap}
.body-copy{font-size:6px;line-height:1.35;color:#333}
.dark-label{background:var(--dark);color:#fff;font-size:7.5px;font-weight:500;display:flex;align-items:center;padding-left:8px}
.bullet{font-size:6px;line-height:1.3;padding-left:10px}
.bullet::before{content:"";position:absolute;left:0;top:1px;border-left:5px solid var(--green);border-top:3.5px solid transparent;border-bottom:3.5px solid transparent}
.table-head{border:1.5px solid var(--green);border-right-width:4px;font-weight:700;font-size:12px;color:var(--ink);display:flex;align-items:center;padding-left:12px;height:22px}
.cell{background:var(--row);height:27px;font-size:8px;display:flex;align-items:center;color:#222}
.cell.code{width:133px;justify-content:center}
.cell.desc{padding-left:14px;font-size:6px;line-height:1.25;font-weight:500}
.rule{height:1px;background:var(--green)}
.feature-rail{width:12px;background:var(--row)}
.feature-icon{width:26px;height:26px;background:linear-gradient(135deg,var(--orange-light),var(--orange))}
.feature-icon svg{position:static;display:block}
.feature-text{font-size:8px;font-weight:500;color:#222;padding-left:10px;white-space:nowrap}
.feature-text::before{content:"";position:absolute;left:0;top:1px;border-left:5px solid var(--green);border-top:3.5px solid transparent;border-bottom:3.5px solid transparent}
.chip{width:87px;height:17px;font-size:8px;padding-left:8px;display:flex;align-items:center;border:1px solid #999}
.contact-item{font-size:6.5px;font-weight:600;color:#222;display:flex;align-items:center;gap:4px;white-space:nowrap;line-height:1.15}
.contact-item i{position:static;width:10px;height:10px;border-radius:50%;background:var(--orange);display:inline-block;flex:none}
.contact-item span{position:static}
.arrows svg{position:static;display:block}
</style>
</head>
<body>

<!-- Cover -->
<section class="page cover">
  <div class="brand" style="left:0;width:678px;top:62px;justify-content:center;font-size:34px">
    <i class="brand-mark" style="width:26px;height:26px"></i><span>VANTRA LAB</span>
  </div>
  <div class="cover-band"></div>
  <h1 class="cover-title">CHEMICAL RESISTANT</h1>
  <h2 class="cover-sub">CERAMIC WORKTOP</h2>
  <div class="cover-tag">FOR LABORATORY FURNITURE</div>
  <div class="photo cover-photo" role="img" aria-label="Photo of white laboratory base cabinets with a black ceramic worktop and a window above"></div>
  <div class="catalog-row flow" style="position:absolute;left:62px;top:793px;gap:16px">
    <span class="catalog-word" style="font-size:30px;letter-spacing:7px">CATALOG</span>
    <span class="year" style="width:78px;height:23px;font-size:19px">2022</span>
  </div>
  <div class="site" style="right:62px;top:799px;font-size:15px">www.vantralab-demo.com</div>
</section>

<!-- PP Fumecupboard -->
<section class="page sheet sheet-pp">
  <div class="frame" style="left:28px;top:28px;width:158px;height:188px"><div class="shot" role="img" aria-label="Photo of a polypropylene fume cupboard with base cabinet"></div></div>
  <div class="h-title" style="left:210px;top:28px;font-size:16px">PP FUMECUPBOARD</div>
  <div class="h-sub" style="left:210px;top:45px">CATEGORY DESCRIPTION</div>
  <p class="body-copy" style="left:210px;top:64px;width:200px">Polypropylene fume hoods are manufactured entirely of structural polypropylene. Polypropylene offers excellent chemical resistant and allows for NO MORE RUST!</p>
  <p class="body-copy" style="left:210px;top:96px;width:200px">Supplied with its own base cabinet, these ranges of fume hoods are built to order and may be coordinated to match existing laboratory furniture upon request.</p>
  <div class="dark-label" style="left:210px;top:131px;width:130px;height:17px">Standard Features Include:</div>
  <p class="bullet" style="left:210px;top:158px;width:200px">Constructed from all white stress relieved, acid resistant, non-corrosive polypropylene. All heat seam welded and tested.</p>
  <p class="bullet" style="left:210px;top:189px;width:200px">Material selection for use with harsh acids and other corrosive applications.</p>
  <p class="bullet" style="left:210px;top:210px;width:200px">Supplied with built in light switch.</p>
  <div style="left:28px;top:232px;width:384px;height:22px;border:1px solid var(--green)"></div>
  <div class="dark-label" style="left:28px;top:232px;width:129px;height:22px">Optional Features Include:</div>
  <p class="bullet" style="left:168px;top:236px;width:236px">Digital air flow monitor with audible and visible alarm functions for constant monitoring of exhaust air.</p>
  <div style="left:28px;top:267px;width:384px;height:63px;background:var(--band)"></div>
  <div style="left:42px;top:276px;font-size:7.5px;font-weight:500;color:#222">PP (Polypropylene) Fumecupboard</div>
  <div style="left:42px;top:292px;width:2px;height:22px;background:var(--green)"></div>
  <p class="body-copy" style="left:54px;top:291px;width:345px">Benchlyn PP Polypropylene fume hoods are manufactured entirely of structural polypropylene. Polypropylene is often chosen for its resistance to corrosion and chemical leaching, it is resilience against most forms of physical damage and allows for NO RUST!</p>
  <div class="table-head" style="left:28px;top:348px;width:133px">PRODUCT CODE</div>
  <div class="table-head" style="left:178px;top:348px;width:133px">DESCRIPTIONS</div>
  <div class="cell code" style="left:28px;top:383px">FC120-0002</div>
  <div class="cell desc" style="left:178px;top:383px;width:234px">1.2M PP General Purpose Fumecupboard<br>With PP Base Cabinet</div>
  <div class="cell code" style="left:28px;top:420px">FC150-0002</div>
  <div class="cell desc" style="left:178px;top:420px;width:234px">1.5M PP General Purpose Fumecupboard<br>With PP Base Cabinet</div>
  <div class="cell code" style="left:28px;top:456px">FC180-0002</div>
  <div class="cell desc" style="left:178px;top:456px;width:234px">1.8M PP General Purpose Fumecupboard<br>With PP Base Cabinet</div>
  <div class="rule" style="left:45px;top:540px;width:95px"></div>
  <div class="site" style="left:145px;top:534px;width:151px;text-align:center;font-size:9.5px">www.vantralab-demo.com</div>
  <div class="rule" style="left:301px;top:540px;width:95px"></div>
</section>

<!-- Benchlyn ceramic worktop -->
<section class="page sheet sheet-benchlyn">
  <div class="h-title" style="left:28px;top:28px;font-size:20px">BENCHLYN</div>
  <div class="h-sub" style="left:28px;top:50px">LABORATORY CERAMIC WORKTOP</div>
  <div class="brand" style="right:29px;top:34px;font-size:12px"><i class="brand-mark" style="width:10px;height:10px"></i><span>VANTRA LAB</span></div>
  <div style="left:28px;top:66px;width:384px;height:1.5px;background:var(--orange)"></div>

  <div class="feature-rail" style="left:28px;top:79px;height:135px"></div>
  <div class="feature-rail" style="left:236px;top:79px;height:135px"></div>

  <div class="feature-icon" style="left:42px;top:91px"><svg width="26" height="26" viewBox="0 0 26 26"><path d="M7 19 L17 9 M15 7 l4 4" stroke="#fff" stroke-width="2" fill="none"/></svg></div>
  <div class="feature-text" style="left:90px;top:100px">Corrosion Resistant</div>
  <div class="feature-icon" style="left:42px;top:122px"><svg width="26" height="26" viewBox="0 0 26 26"><rect x="7" y="7" width="12" height="12" fill="none" stroke="#fff" stroke-width="2"/><path d="M7 19 L19 7" stroke="#fff" stroke-width="1.5"/></svg></div>
  <div class="feature-text" style="left:90px;top:131px">Scratch Resistant</div>
  <div class="feature-icon" style="left:42px;top:153px"><svg width="26" height="26" viewBox="0 0 26 26"><path d="M13 5 C17 10 17 13 13 17 C9 13 9 10 13 5Z" fill="#fff"/><path d="M6 20h14" stroke="#fff" stroke-width="2"/></svg></div>
  <div class="feature-text" style="left:90px;top:162px">Fireproof up to 1200 C</div>
  <div class="feature-icon" style="left:42px;top:183px"><svg width="26" height="26" viewBox="0 0 26 26"><circle cx="9" cy="9" r="2.5" fill="#fff"/><circle cx="17" cy="17" r="2.5" fill="#fff"/><path d="M18 7 L8 19" stroke="#fff" stroke-width="2"/></svg></div>
  <div class="feature-text" style="left:90px;top:192px">Antibacterial</div>

  <div class="feature-icon" style="left:249px;top:91px"><svg width="26" height="26" viewBox="0 0 26 26"><rect x="7" y="7" width="12" height="12" rx="2" fill="none" stroke="#fff" stroke-width="2"/></svg></div>
  <div class="feature-text" style="left:297px;top:100px">Non-deformation</div>
  <div class="feature-icon" style="left:249px;top:122px"><svg width="26" height="26" viewBox="0 0 26 26"><circle cx="13" cy="14" r="5" fill="none" stroke="#fff" stroke-width="2"/><path d="M13 5v4" stroke="#fff" stroke-width="2"/></svg></div>
  <div class="feature-text" style="left:297px;top:131px">Easy to clean</div>
  <div class="feature-icon" style="left:249px;top:153px"><svg width="26" height="26" viewBox="0 0 26 26"><path d="M13 5 C18 11 18 15 13 20 C8 15 8 11 13 5Z" fill="#fff"/></svg></div>
  <div class="feature-text" style="left:297px;top:162px">Non-inflamable Class 1A</div>
  <div class="feature-icon" style="left:249px;top:183px"><svg width="26" height="26" viewBox="0 0 26 26"><path d="M8 8 C10 11 10 13 8 15 C6 13 6 11 8 8Z M13 8 C15 11 15 13 13 15 C11 13 11 11 13 8Z M18 8 C20 11 20 13 18 15 C16 13 16 11 18 8Z" fill="#fff"/><path d="M6 19h14" stroke="#fff" stroke-width="2"/></svg></div>
  <div class="feature-text" style="left:297px;top:192px">Waterproof</div>

  <div class="h-title" style="left:30px;top:236px;font-size:15px">CERAMIC TOP</div>
  <div class="h-sub" style="left:30px;top:252px">CATEGORY DESCRIPTION</div>
  <div style="left:29px;top:273px;width:194px;height:132px;border:1px solid var(--green)"></div>
  <div class="photo" style="left:41px;top:279px;width:78px;height:58px" role="img" aria-label="Photo of a white laboratory bench room"></div>
  <div class="photo" style="left:125px;top:279px;width:85px;height:58px" role="img" aria-label="Photo of island lab benches with reagent shelves"></div>
  <div class="photo" style="left:41px;top:342px;width:78px;height:58px" role="img" aria-label="Photo of black ceramic worktop benches"></div>
  <div style="left:155px;top:357px;width:13px;height:13px;background:#eee"></div>
  <div style="left:163px;top:365px;width:13px;height:13px;background:#e2e2e2"></div>
  <div style="left:25px;top:336px;width:8px;height:12px;border-radius:50%;background:var(--green)"></div>
  <div style="left:219px;top:380px;width:8px;height:12px;border-radius:50%;background:var(--green)"></div>
  <div class="frame" style="left:238px;top:236px;width:172px;height:169px"><div class="shot photo" role="img" aria-label="Photo of white cabinets with black ceramic worktop"></div></div>

  <div style="left:28px;top:430px;width:384px;height:22px;border:1px solid var(--green)"></div>
  <div style="left:156px;top:430px;width:256px;height:22px;background:var(--green)"></div>
  <div class="h-title" style="left:40px;top:435px;font-size:12px">COLOURS</div>
  <div class="chip" style="left:28px;top:463px;background:#fff;border-color:var(--orange)">White</div>
  <div class="chip" style="left:28px;top:485px;background:#cfcfd4">Grey</div>
  <div class="chip" style="left:28px;top:507px;background:var(--ink);color:#fff">Black</div>
  <p class="body-copy" style="left:128px;top:463px;width:272px">Benchlyn laboratory 15mm ceramic worktop are sintered at a high temperature of 1200 °C can truly achieve the same color of the body and glaze and avoid problems such as delamination and shedding. Ceramic worktop is corrosion-resistant, fireproof, waterproof, scratch-resistant, abrasion-resistant, non-deformation.</p>
  <p class="body-copy" style="left:128px;top:505px;width:272px">Ceramic worktops can resist strong acid, alkaline and organic solvent corrosion (except for hydrofluoric acid equivalent chemical reagents).</p>
  <div class="site" style="right:29px;top:534px;font-size:10px">www.vantralab-demo.com</div>
</section>

<!-- Our categories -->
<section class="page sheet sheet-categories">
  <div class="h-title" style="left:28px;top:26px;font-size:21px">OUR <span style="position:static;color:var(--green)">CATEGORIES</span></div>
  <p class="body-copy" style="left:28px;top:58px;width:384px;font-weight:700">Our ceramic worktop was chemical resistant, is a good worktop material for high chemicals corrosion environment like laboratory furniture, fumecupboard.</p>
  <div class="frame" style="left:28px;top:85px;width:158px;height:170px"><div class="shot" role="img" aria-label="Photo of a general purpose fume cupboard with base cabinet"></div></div>
  <div class="h-title" style="left:210px;top:84px;font-size:16px">FUMECUPBOARD</div>
  <div class="h-sub" style="left:210px;top:101px">CATEGORY DESCRIPTION</div>
  <p class="body-copy" style="left:210px;top:119px;width:202px">Fume cupboard, often known as fume hoods, fume filtration or fume cabinets. Usually, they are located in the smoke extraction system installed in the scientific laboratories and physicians to protect users from harmful substances can be inhaled. All laboratory work which involved gases, fumes, particles or liquids that are handled in dangerous quantities and concentrations must be performed in fume cupboards to avoid any accidents happen.</p>
  <p class="body-copy" style="left:210px;top:185px;width:202px">Most of the fume cupboard are designed connecting to exhaust systems that expel the air way to the external of a building, a large amount of energy required to run fans that exhaust the air, and to heat, cool, filter, control and move the fresh air that will replace the air exhausted. Recently, laboratory manufacturer had been working on fume cupboard and ventilation system design which focused on reducing the energy used to operate fume cupboard and their supporting ventilation systems.</p>
  <p class="body-copy" style="left:28px;top:268px;width:384px">There are several factors that influence how effectively a fume cupboard will contain vapours. All users should be aware of these to ensure the fume cupboard is set up to minimise these effects. Schools and related departments have the responsible to ensure the staff and students have been fully briefed on the correct operation step before beginning work. Make sure they have read and signed off on the guidance document. After using fume cupboard, leave it in a clean and safe condition for next user. When the work is completed, ensure that redundant equipment is removed and the fume cupboard surfaces are cleaned without any chemical left.</p>
  <div class="table-head" style="left:28px;top:328px;width:133px">PRODUCT CODE</div>
  <div class="table-head" style="left:178px;top:328px;width:133px">DESCRIPTIONS</div>
  <div class="cell code" style="left:28px;top:364px">FC120-0002</div>
  <div class="cell desc" style="left:178px;top:364px;width:234px">1.2M General Purpose E.G. Fumecupboard<br>With Base Cabinet</div>
  <div class="cell code" style="left:28px;top:401px">FC150-0002</div>
  <div class="cell desc" style="left:178px;top:401px;width:234px">1.5M General Purpose E.G. Fumecupboard<br>With Base Cabinet</div>
  <div class="cell code" style="left:28px;top:437px">FC180-0002</div>
  <div class="cell desc" style="left:178px;top:437px;width:234px">1.8M General Purpose E.G. Fumecupboard<br>With Base Cabinet</div>
  <div style="left:28px;top:478px;width:384px;height:63px;background:var(--band)"></div>
  <div style="left:42px;top:487px;width:2px;height:34px;background:var(--green)"></div>
  <p class="body-copy" style="left:55px;top:485px;width:345px">All fumecupboards are designed and manufactured in close liaison with the customer and their requirements. Factors such as the likely use of the fumecupboard (Acid, Organic chemistry, Radioactivity) and its location all play a part in the overall design and specification of the unit. Our professional team can advise on any aspect of the systems performance whether it be the materials of construction or the airflow performance and the resultant extract system.</p>
  <div style="left:55px;top:536px;width:200px;height:1px;background:var(--orange)"></div>
  <div class="site" style="right:35px;top:530px;font-size:9.5px">www.vantralab-demo.com</div>
</section>

<!-- Back cover -->
<section class="page sheet sheet-back">
  <div style="left:0;top:0;width:441px;height:401px;background:linear-gradient(160deg,#f3b04c 0%,#e9a23a 35%,#2a1a08 48%,#f6d9a6 62%,#e8a448 100%)" role="img" aria-label="Orange-toned photo of white laboratory cabinets with a black ceramic worktop"></div>
  <div class="brand" style="left:170px;top:336px;font-size:21px"><i class="brand-mark" style="width:16px;height:16px"></i><span>VANTRA LAB</span></div>
  <div style="left:28px;top:428px;width:112px;height:19px;border:1.5px solid var(--green)"></div>
  <div class="h-title" style="left:40px;top:432px;font-size:11px">CONTACT US</div>
  <div class="arrows" style="left:158px;top:434px"><svg width="40" height="8" viewBox="0 0 40 8" fill="#1aab3a"><path d="M0 0l6 4-6 4z M8 0l6 4-6 4z M16 0l6 4-6 4z M24 0l6 4-6 4z M32 0l6 4-6 4z"/></svg></div>
  <div class="contact-item" style="left:215px;top:433px"><i></i><span>603 5550 0101</span></div>
  <div class="contact-item" style="left:320px;top:433px"><i></i><span>603 5550 0102</span></div>
  <div class="contact-item" style="left:28px;top:461px"><i></i><span><b style="font-size:5.5px">SKYPE</b><br>vls0101</span></div>
  <div class="contact-item" style="left:120px;top:461px"><i></i><span>6012 555 0155<br>603 5550 0102</span></div>
  <div class="contact-item" style="left:215px;top:463px"><i></i><span>ww.vantralab-demo.com</span></div>
  <div class="contact-item" style="left:320px;top:463px"><i></i><span>info@vantralab-demo.com</span></div>
  <div class="arrows" style="left:372px;top:494px"><svg width="40" height="8" viewBox="0 0 40 8" fill="#1aab3a"><path d="M6 0l-6 4 6 4z M14 0l-6 4 6 4z M22 0l-6 4 6 4z M30 0l-6 4 6 4z M38 0l-6 4 6 4z"/></svg></div>
  <div class="catalog-row flow" style="position:absolute;left:28px;top:522px;gap:10px">
    <span class="catalog-word" style="font-size:20px;letter-spacing:4px">CATALOG</span>
    <span class="year" style="width:48px;height:15px;font-size:12px;letter-spacing:2px">2022</span>
  </div>
  <div class="site" style="right:29px;top:527px;font-size:10px">www.vantralab-demo.com</div>
  <div style="left:0;top:561px;width:441px;height:9px;background:var(--ink)"></div>
</section>

</body>
</html>
```